Honey apple cider vinegar label

organic food company need a contemporary honey apple cider vinegar and honey vinegar label, natural GMP logo HACCP LOgo
label detail height :140mm Width:80mm
ingredient: honey, apple cider vinegar and water, free from artificial color & preservative
Shelf Life: 3 years
Net weight 400ml
Storage : store in cool place , do not expose to sunlight
instruction for use: add 20ml to a full glass of water 3, times a days before meal, stop consuming if allergies happen
certification, GMP HACCP, Halal, natural product

Target Market(s)

health conscious group

Requirements
Must have
• modern feel, honey and apple picture

```html
<!DOCTYPE html>
<html lang="en">
<head>
<meta charset="utf-8">
<title>melora Honey Apple Cider Vinegar Label</title>
<link rel="stylesheet" href="https://fonts.googleapis.com/css2?family=Open+Sans:wght@400;600;700;800&family=Arimo:wght@400&display=swap">
<style>
:root{
  --purple:#4210c4;
  --gold:#d9a62e;
  --honey:#ffe24a;
  --amber:#f7a41a;
  --white:#ffffff;
  --star:#f2c232;
}
*{box-sizing:border-box;margin:0;padding:0}
html,body{width:1074px;height:1200px;overflow:hidden;background:var(--white)}
.label{position:absolute;left:232px;top:115px;width:605px;height:1058px;background:var(--purple);overflow:hidden;font-family:"Arimo",Arial,sans-serif;color:var(--white)}
.front{position:absolute;left:0;top:0;width:605px;height:647px}
.honey-band{position:absolute;left:0;top:0;width:605px;height:120px;background:linear-gradient(180deg,var(--honey) 0%,#fcc83a 45%,var(--amber) 70%,rgba(66,16,196,0) 100%)}
.brand-mark{position:absolute;left:257px;top:150px;width:92px;height:92px;border-radius:50%;background:var(--purple)}
.brand-name{position:absolute;left:0;width:605px;top:262px;text-align:center;font-family:"Open Sans",Arial,sans-serif;font-weight:800;font-size:92px;line-height:1;color:var(--purple);letter-spacing:-1px}
.hero{position:absolute;left:139px;top:372px;width:336px;height:250px;border-radius:46% 54% 48% 52%/50% 40% 60% 50%;background:linear-gradient(120deg,#c63a56 0%,#e8a63a 45%,#9fd94a 75%,#e8f7d8 100%)}
.net-weight{position:absolute;left:84px;top:604px;width:115px;height:23px;border:2px solid var(--gold);border-radius:8px;background:var(--purple);font-family:"Open Sans",Arial,sans-serif;font-size:12.5px;line-height:19px;text-align:center}
.gold-rule{position:absolute;left:0;top:647px;width:605px;height:10px;background:linear-gradient(var(--gold),#fff3c4 45%,var(--gold))}
.stars{position:absolute;left:0;width:605px;text-align:center;line-height:0}
.usage{position:absolute;left:0;top:700px;width:605px;text-align:center}
.usage h2{font-family:"Open Sans",Arial,sans-serif;font-weight:700;font-size:20px;line-height:26px}
.usage p{margin-top:0;font-size:15.4px;line-height:22px}
.jar-art{position:absolute;border-radius:18px;background:linear-gradient(160deg,#f08fbf 0%,#f57a45 40%,#f6b21c 100%);opacity:.85}
.details{position:absolute;left:10px;top:801px;width:584px;height:161px;background:var(--white);border:2px solid var(--gold);color:var(--purple)}
.details .item{position:absolute;left:23px}
.details h3{font-family:"Open Sans",Arial,sans-serif;font-weight:400;font-size:19px;line-height:22px;white-space:nowrap}
.details p{font-size:15.4px;line-height:19px;white-space:nowrap}
.footer-cert{position:absolute;left:24px;top:980px;width:113px;height:61px;background:var(--white)}
.cert-text{position:absolute;left:160px;top:988px;font-size:13px;line-height:18px;white-space:nowrap}
.cert-text strong{font-family:"Open Sans",Arial,sans-serif;font-weight:700;font-size:15px}
.seal{position:absolute;left:498px;top:969px;width:80px;height:80px;border-radius:50%;background:var(--gold)}
</style>
</head>
<body>
<div class="label">
  <svg class="front" viewBox="0 0 605 647" aria-hidden="true">
    <path d="M0,160 L129,201 Q302,6 478,199 L605,155 L605,185 L525,215 L525,647 L70,647 L70,215 L0,190 Z" fill="#fff"/>
    <path d="M0,160 L129,201 Q302,6 478,199 L605,155" fill="none" stroke="#d9a62e" stroke-width="3"/>
  </svg>
  <div class="honey-band" role="img" aria-label="Decorative honey drip border across the top of the label"></div>
  <div class="brand-mark"></div>
  <div class="brand-name">melora</div>
  <div class="hero" role="img" aria-label="Illustration of two red apples with honey dripping from a honey dipper over green leaves"></div>
  <div class="net-weight">Net weight 400ml</div>
  <div class="gold-rule"></div>

  <div class="stars" style="top:672px">
    <svg width="130" height="26" viewBox="0 0 130 26"><defs><polygon id="star" points="0,-10 2.35,-3.24 9.51,-3.09 3.8,1.24 5.88,8.09 0,4 -5.88,8.09 -3.8,1.24 -9.51,-3.09 -2.35,-3.24" fill="#f2c232"/></defs>
      <use href="#star" transform="translate(12,14) scale(.9)"/><use href="#star" transform="translate(38,14) scale(.9)"/><use href="#star" transform="translate(65,13) scale(1.25)"/><use href="#star" transform="translate(92,14) scale(.9)"/><use href="#star" transform="translate(118,14) scale(.9)"/></svg>
  </div>
  <div class="jar-art" style="left:28px;top:688px;width:84px;height:82px" role="img" aria-label="Small illustration of a honey jar with flowers and a honey dipper"></div>
  <div class="jar-art" style="left:492px;top:688px;width:84px;height:82px" role="img" aria-label="Small illustration of a honey jar with flowers and a honey dipper"></div>
  <div class="usage">
    <h2>Instruction for use</h2>
    <p>Add 20ml to a full glass of water 3, times a<br>days before meal, stop consuming if allergies<br>happen.</p>
  </div>

  <div class="details">
    <div class="item" style="top:3px"><h3>Ingredient:</h3></div>
    <div class="item" style="top:30px"><p>Honey, apple cider vinegar and water, free from artificial color &amp; preservative.</p></div>
    <div class="item" style="top:60px"><h3>Shelf Life:</h3></div>
    <div class="item" style="top:81px"><p>3 years</p></div>
    <div class="item" style="top:112px"><h3>Storage :</h3></div>
    <div class="item" style="top:133px"><p>Store in cool place , do not expose to sunlight</p></div>
  </div>
  <div class="jar-art" style="left:404px;top:865px;width:88px;height:84px" role="img" aria-label="Small illustration of a honey jar with flowers and a honey dipper"></div>

  <div class="footer-cert"></div>
  <div class="cert-text"><strong>Certification:</strong> GMP, HACCP, Halal, Natural product</div>
  <div class="stars" style="top:1013px">
    <svg width="160" height="32" viewBox="0 0 160 32">
      <use href="#star" transform="translate(14,17) scale(1.1)"/><use href="#star" transform="translate(46,17) scale(1.1)"/><use href="#star" transform="translate(80,16) scale(1.5)"/><use href="#star" transform="translate(114,17) scale(1.1)"/><use href="#star" transform="translate(146,17) scale(1.1)"/></svg>
  </div>
  <div class="seal"></div>
</div>
</body>
</html>
```